Everett's Book Cover

Need a cover design for a book (paperback and eBook)
Book Title: Where The Cedar Rivers Bend
Book Width: 15.24
Book Height: 22.86
Thickness: approximately 200 pages.
Book is a collection of stories drawn from the author's life, and will be in the local history genre in northern British Columbia, Canada from the period 1930 to the present time.
Author: Everett Hollis Pelletier
Must include "As told to Marnie Kowal" on front cover, not on the spine.
Author invites designers creativity and asks that the attached photos be incorporated into the front and back covers in tasteful ways as follows:
Other uses of the photos will be considered.
We apologize for the quality of the photos. Please do what you can.
We look forward to your designs.
Thank you for considering.

Target Market(s)

Lovers of local history, jokes, storytelling, back country hiking and mountain climbing. Men and women 30 years and older. Primary target readership are men and women in their 40's, 50's, 60's, and older, who love local history

Font styles to use
Sans Serif

Requirements
Must have
• Back cover copy must clear and easy to read.
Must appeal to outdoor, back country types.
Nice to have
• Like to see a creative incorporation of the photos provided.
Build on or compliment the colours in the photos

```html
<!DOCTYPE html>
<html lang="en">
<head>
<meta charset="utf-8">
<title>Where The Cedar Rivers Bend – Cover</title>
<link rel="stylesheet" href="https://fonts.googleapis.com/css2?family=Jost:wght@400;500;700;800&display=swap">
<style>
  :root {
    --olive: #5e6b00;
    --cream: #f0e5d5;
    --white: #ffffff;
    --ink: #111111;
    --text: #1a1a1a;
  }
  * { margin: 0; padding: 0; box-sizing: border-box; }
  html, body { width: 1200px; height: 770px; overflow: hidden; background: var(--white); }
  .cover { position: relative; width: 1200px; height: 770px; font-family: 'Jost', sans-serif; overflow: hidden; }
  .block { position: absolute; }
  .cream { background: var(--cream); }
  .olive { background: var(--olive); }
  .photo { position: absolute; }

  /* back cover */
  .back-panel { left: 0; top: 0; width: 513px; height: 770px; }
  .back-top-bar { left: 32px; top: 0; width: 236px; height: 27px; }
  .photo-author { left: 34px; top: 46px; width: 235px; height: 350px;
    background: linear-gradient(180deg, #6f8d52 0%, #4f8a2e 35%, #3d7a25 60%, #557a35 100%); }
  .author-heading { position: absolute; left: 280px; top: 44px; width: 220px;
    color: var(--olive); font-size: 13.5px; font-weight: 400; line-height: 16px; text-transform: uppercase; }
  .heading-rule { position: absolute; left: 270px; top: 78px; width: 242px; height: 1px; background: var(--text); }
  .bio { position: absolute; left: 281px; top: 85px; width: 222px;
    color: var(--text); font-size: 7.6px; line-height: 12.7px; font-weight: 400; }
  .bio p + p { margin-top: 12.7px; }
  .back-left-bar { left: 0; top: 420px; width: 87px; height: 350px; }
  .back-title { position: absolute; left: 135px; top: 418px; color: var(--olive);
    font-weight: 700; font-size: 36px; line-height: 49px; text-transform: uppercase;
    letter-spacing: 0.3px; white-space: nowrap; }
  .back-right-bar { left: 426px; top: 575px; width: 87px; height: 195px; }
  .photo-bear { left: 128px; top: 580px; width: 257px; height: 190px;
    background: linear-gradient(180deg, #8a9aa6 0%, #8c7a64 25%, #bfc2b9 60%, #e4e6e3 100%); }

  /* spine */
  .spine { left: 541px; top: 0; width: 117px; height: 770px; }
  .spine-author { position: absolute; left: 608px; top: 38px; transform-origin: 0 0; transform: rotate(90deg);
    color: var(--cream); font-size: 17px; font-weight: 400; white-space: nowrap; letter-spacing: 0.3px; }
  .spine-title { position: absolute; left: 614px; top: 283px; transform-origin: 0 0; transform: rotate(90deg);
    color: var(--ink); font-size: 29px; font-weight: 700; white-space: nowrap; }

  /* front cover */
  .front-panel { left: 687px; top: 0; width: 513px; height: 770px; }
  .photo-meadow { left: 726px; top: 0; width: 435px; height: 544px;
    background: linear-gradient(180deg, #4b70b8 0%, #9eb3d4 22%, #c9cfd4 32%, #8e9560 42%, #7a8a3a 60%, #6f8030 80%, #8a8a40 100%); }
  .front-title { position: absolute; left: 773px; top: 30px; color: var(--ink);
    font-weight: 800; font-size: 37px; line-height: 49px; text-transform: uppercase;
    white-space: nowrap; text-shadow: -2px 2px 0 var(--white); }
  .told-to { position: absolute; left: 775px; top: 197px; color: var(--ink);
    font-weight: 700; font-size: 17px; letter-spacing: 0.3px; white-space: nowrap;
    text-shadow: -1px 1px 0 rgba(255,255,255,0.6); }
  .author-plate { position: absolute; left: 785px; top: 490px; width: 320px; height: 36px;
    background: rgba(240, 229, 213, 0.45); border-radius: 10px;
    display: flex; align-items: center; justify-content: center;
    color: var(--ink); font-size: 20px; font-weight: 400; white-space: nowrap; }
  .front-left-bar { left: 687px; top: 575px; width: 87px; height: 195px; }
  .photo-hiker { left: 808px; top: 575px; width: 271px; height: 195px; border-radius: 4px 4px 0 0;
    background: linear-gradient(180deg, #5d7a3a 0%, #6f8a45 45%, #8e8a5e 75%, #6f6a50 100%); }
  .front-right-bar { left: 1113px; top: 575px; width: 87px; height: 195px; }
</style>
</head>
<body>
<div class="cover">
  <!-- back cover -->
  <div class="block cream back-panel"></div>
  <div class="block olive back-top-bar"></div>
  <div class="photo photo-author" role="img" aria-label="Photo of the author and a companion standing in an alpine meadow of wildflowers"></div>
  <h2 class="author-heading">Everett Hollis<br>Pelletier</h2>
  <div class="heading-rule"></div>
  <div class="bio">
    <p>Everett Pelletier is a true old-fashioned story teller. He loves nothing better than a good story, and particularly when he is the one telling the story. He was born and raised in the tiny sawmill town of Larchford, BC and spent 80 years of his life there before relocating to his current home on the banks of the Tallow River in Fort Aldous, BC. In addition to writing this book, Everett spends his time writing songs, singing, telling jokes, and entertaining his many friends with stories of days gone by.</p>
    <p>At the age of 15 he started his career as a flunky in the cookhouse, then moved on to work as a horse logger, sawmill worker, bush foreman, rancher, cat skinner, forest warden, road and bridge builder, and finished his career as salmon hatchery manager.</p>
    <p>Everett's love of the mountains is evident throughout the book, as is his love for the majestic grizzly bears who inhabit them. He spent his spare time mountain climbing, fishing, skiing, snowshoeing, and hiking in the woods near his home. This book is an eclectic collection of stories about family, friends, and adventures, all sprinkled with the author's unique sense of humour.</p>
  </div>
  <div class="block olive back-left-bar"></div>
  <h2 class="back-title">Where<br>The Cedar Rivers<br>Bend</h2>
  <div class="block olive back-right-bar"></div>
  <div class="photo photo-bear" role="img" aria-label="Photo of a grizzly bear on a snowy alpine slope"></div>

  <!-- spine -->
  <div class="block olive spine"></div>
  <div class="spine-author">Everett Hollis Pelletier</div>
  <div class="spine-title">Where The Cedar Rivers Bend</div>

  <!-- front cover -->
  <div class="block cream front-panel"></div>
  <div class="photo photo-meadow" role="img" aria-label="Photo of a mountain meadow with lilies and snow-capped peaks under a blue sky"></div>
  <h1 class="front-title">Where<br>The Cedar Rivers<br>Bend</h1>
  <p class="told-to">As told to Marnie Kowal</p>
  <div class="author-plate">Everett Hollis Pelletier</div>
  <div class="block olive front-left-bar"></div>
  <div class="photo photo-hiker" role="img" aria-label="Photo of a hiker with a backpack on a forest trail"></div>
  <div class="block olive front-right-bar"></div>
</div>
</body>
</html>
```